Vereins Website
Zielgruppe
Webiste für den Verein 'Katzenhain Oberlau' (details siehe Anhang).
Ziel der Website:
- Sponsoren finden
- Vereinsmitglieder finden & Interessen bündeln.
Aufgabenstellung
Die Webiste sollt aufgeräumt, übersichtlich und freundlich wirken.

```html
<!DOCTYPE html>
<html lang="de">
<head>
<meta charset="utf-8">
<title>Verein Katzenhain Oberlau</title>
<link href="https://fonts.googleapis.com/css2?family=Arimo:wght@400;700&display=swap" rel="stylesheet">
<style>
:root{
  --orange:#f29100;
  --orange-soft:#f7c98a;
  --ink:#222;
  --field:#e3e3e3;
  --tile:#e0e0e0;
  --tile-dark:#bdbdbd;
  --band-grey:#e6e6e6;
  --footer:#7a7a7a;
  --white:#fff;
}
*{box-sizing:border-box;margin:0;padding:0}
html,body{width:1200px;height:3345px;overflow:hidden}
body{position:relative;background:var(--white);font-family:"Arimo",Arial,sans-serif;color:var(--ink)}
.abs{position:absolute}
.center{left:0;width:1200px;text-align:center}
.site-header{top:0;left:0;width:1200px;height:160px;background:var(--orange)}
.site-header .kicker{top:66px;font-size:18px;letter-spacing:8px;color:#333}
.site-header .brand{top:92px;font-size:40px;font-weight:700;letter-spacing:2px;color:var(--white);text-transform:uppercase}
.hero{top:160px;left:0;width:1200px;height:620px;background:linear-gradient(180deg,#b9bbbd 0%,#a7aaa8 30%,#7a7b5f 52%,#6b7a3f 62%,#4d7a2c 100%)}
.hero h1{top:572px;font-size:33px;line-height:40px;letter-spacing:1.5px;color:var(--white);font-weight:700;text-shadow:0 1px 3px rgba(0,0,0,.5)}
.btn{display:flex;align-items:center;justify-content:center;font-size:10px;font-weight:700;letter-spacing:2.5px;text-transform:uppercase}
.btn-orange{background:var(--orange);color:var(--white)}
.btn-white{background:var(--white);color:var(--ink)}
.intro h2{top:848px;font-size:33px;line-height:40px;letter-spacing:1.5px;color:var(--orange);font-weight:700}
.intro p{top:948px;font-size:12px;line-height:18.8px;letter-spacing:3px}
.form-title{top:1150px;font-size:21px;font-weight:700;letter-spacing:1.5px}
.label{font-size:12px;letter-spacing:2.5px}
.field{background:var(--field)}
.note{top:1525px;font-size:12.5px;line-height:17px;letter-spacing:.6px}
.help h2{top:1690px;font-size:40px;font-weight:700;letter-spacing:2px;color:var(--orange)}
.help .sub{top:1738px;font-size:24px;letter-spacing:5px}
.photo-dog{left:340px;top:1808px;width:510px;height:200px;border-radius:200px 200px 0 0;background:linear-gradient(180deg,#a45a22,#c9762f 55%,#5a3418)}
.account{top:2008px;left:0;width:1200px;height:218px;background:var(--orange);color:var(--white)}
.account .t{top:44px;font-size:29px;font-weight:700;letter-spacing:1px}
.account .l{font-size:19px;letter-spacing:1px}
.section-title{font-size:29px;font-weight:700;letter-spacing:2px}
.tile{background:var(--tile)}
.tile-feature{background:var(--tile-dark);color:var(--white);display:flex;align-items:center;justify-content:center;text-align:center;font-size:18px;line-height:23px;letter-spacing:1px}
.small{font-size:11px;letter-spacing:.4px;color:#444}
.pay{display:flex;align-items:center;justify-content:center;gap:6px;font-size:17px;font-weight:700}
.pay .sq{width:12px;height:12px;background:currentColor}
.feedback{top:2873px;left:0;width:1200px;height:422px;background:var(--band-grey)}
.feedback h3{top:57px;font-size:19px;font-weight:700;letter-spacing:1.5px}
.photo-puppy{left:140px;top:97px;width:385px;height:275px;border-radius:45% 50% 40% 40%;background:radial-gradient(ellipse at 50% 45%,#f4efe6,#e2d8c8 70%,rgba(230,230,230,0) 100%)}
.input{background:var(--white);font-size:11px;letter-spacing:2.5px;color:#444;padding:10px 13px}
.check{font-size:10px;color:#333;display:flex;align-items:center;gap:7px}
.check .box{width:14px;height:14px;border:1px solid #888;background:var(--white)}
.site-footer{top:3295px;left:0;width:1200px;height:50px;background:var(--footer);color:var(--white);font-size:14px;letter-spacing:.8px;display:flex;align-items:center;justify-content:center}
</style>
</head>
<body>

<header class="site-header abs">
  <div class="kicker abs center">VEREIN</div>
  <div class="brand abs center">Katzenhain Oberlau</div>
</header>

<section class="hero abs" role="img" aria-label="Foto: eingezäunte Spielwiese mit Sonnensegel, Bäumen und Besuchern mit ihren Tieren">
</section>
<h1 class="abs center" style="top:572px;font-size:33px;line-height:40px;letter-spacing:1.5px;color:#fff;text-shadow:0 1px 3px rgba(0,0,0,.5)">WERDEN SIE VEREINSMITGLIED UND<br>UNTERSTÜTZEN UNSER PROJEKT</h1>
<a class="btn btn-orange abs" style="left:409px;top:678px;width:176px;height:32px">Mitglied werden</a>
<a class="btn btn-white abs" style="left:625px;top:678px;width:176px;height:32px">Sponsor werden</a>

<section class="intro">
  <h2 class="abs center">EIN BEGEGNUNGSORT FÜR DIE GANZE REGION,<br>VON DEM ALLE PROFITIEREN.</h2>
  <p class="abs center">NACH DEM VORBILD VON <b>WALDSTETTEN</b> MÖCHTEN WIR IN OBERLAU EINE<br>EINGEZÄUNTE SPIELWIESE AUF DIE BEINE STELLEN UND DAMIT<br>DAS WOHLERGEHEN DER TIERE FÖRDERN.<br>AUF DER EINGEZÄUNTEN WIESE KÖNNEN DIE TIERE OHNE LEINENZWANG SPIELEN, SICH<br>AUSTOBEN UND SOZIALISIEREN.<br>GLEICHZEITIG SCHAFFT DIES EINEN RAUM, IN DEM SICH DIE TIERHALTER TREFFEN UND<br>AUSTAUSCHEN KÖNNEN.</p>
</section>

<section class="membership">
  <div class="form-title abs center">PROJEKT UNTERSTÜTZEN UND VEREINSMITGLIED* WERDEN:</div>
  <div class="label abs" style="left:304px;top:1207px">VORNAME</div>
  <div class="label abs" style="left:623px;top:1207px">NACHNAME</div>
  <div class="field abs" style="left:295px;top:1231px;width:301px;height:37px"></div>
  <div class="field abs" style="left:614px;top:1231px;width:301px;height:37px"></div>
  <div class="label abs" style="left:304px;top:1285px">STRASSE | HAUSNUMMER</div>
  <div class="field abs" style="left:295px;top:1309px;width:620px;height:37px"></div>
  <div class="label abs" style="left:304px;top:1364px">PLZ | ORT</div>
  <div class="field abs" style="left:295px;top:1388px;width:620px;height:37px"></div>
  <div class="label abs" style="left:304px;top:1442px">E-MAIL-ADRESSE</div>
  <div class="field abs" style="left:295px;top:1466px;width:620px;height:37px"></div>
  <div class="note abs center">* EINE VEREINSMITGLIEDSCHAFT IST DERZEIT NOCH KOSTENLOS.<br>SIE UNTERSTÜTZEN DEN VEREIN DAMIT IDEELL.</div>
  <a class="btn btn-orange abs" style="left:499px;top:1579px;width:177px;height:31px;font-weight:400">Absenden</a>
</section>

<section class="help">
  <h2 class="abs center">HELFEN SIE UNS</h2>
  <div class="sub abs center">DIESES PROJEKT ZU VERWIRKLICHEN</div>
  <div class="photo-dog abs" role="img" aria-label="Foto: Tier schaut neugierig über den Rand"></div>
</section>

<section class="account abs">
  <div class="t abs center">SPENDENKONTO:</div>
  <div class="l abs center" style="top:96px">KATZENHAIN OBERLAU</div>
  <div class="l abs center" style="top:134px">IBAN: 98 00000 00000 00000 9</div>
  <div class="l abs center" style="top:172px">BIC: 6553873</div>
</section>

<section class="sponsors">
  <div class="section-title abs center" style="top:2277px">FÜR SPONSOREN</div>
  <div class="tile abs" style="left:343px;top:2339px;width:121px;height:122px"></div>
  <div class="tile abs" style="left:480px;top:2339px;width:121px;height:122px"></div>
  <div class="tile-feature abs" style="left:616px;top:2339px;width:260px;height:122px">HIER KÖNNTE<br>IHR LOGO STEHEN</div>
  <div class="tile abs" style="left:343px;top:2474px;width:258px;height:122px"></div>
  <div class="tile abs" style="left:616px;top:2474px;width:122px;height:122px"></div>
  <div class="tile abs" style="left:754px;top:2474px;width:122px;height:122px"></div>
</section>

<section class="private">
  <div class="section-title abs center" style="top:2650px">FÜR PRIVTE SPENDEN</div>
  <div class="small abs center" style="top:2692px;font-weight:700">SPENDENKONTO:</div>
  <div class="small abs center" style="top:2708px">KATZENHAIN OBERLAU · IBAN: 98 00000 00000 00000 9 · BIC: 6553873</div>
  <div class="pay abs" style="left:330px;top:2759px;width:80px;height:55px;color:#111"><span class="sq"></span>Zahlio</div>
  <div class="pay abs" style="left:423px;top:2759px;width:152px;height:55px;color:#111">Postkasse</div>
  <div class="pay abs" style="left:600px;top:2759px;width:130px;height:55px;color:#1f3a78">Netzpay</div>
  <div class="abs" style="left:751px;top:2772px;width:129px;height:31px;background:var(--orange-soft);font-size:9px;display:flex;align-items:center;justify-content:center;color:#333">EINZAHLUNGSSCHEIN</div>
</section>

<section class="feedback abs">
  <h3 class="abs center">WIR FREUEN UNS AUF IHRE ANREGUNGEN &amp; IDEEN:</h3>
  <div class="photo-puppy abs" role="img" aria-label="Foto: junges helles Tier liegt entspannt"></div>
  <div class="input abs" style="left:537px;top:104px;width:172px;height:30px">VORNAME</div>
  <div class="input abs" style="left:716px;top:104px;width:167px;height:30px">NACHNAME</div>
  <div class="input abs" style="left:537px;top:151px;width:346px;height:31px">E-MAIL-ADRESSE</div>
  <div class="input abs" style="left:537px;top:196px;width:346px;height:65px">IHRE NACHRICHT</div>
  <div class="check abs" style="left:550px;top:275px"><span class="box"></span>Kopie an meine E-Mail-Adresse senden</div>
  <a class="btn btn-orange abs" style="left:609px;top:323px;width:192px;height:32px;font-weight:400">Absenden</a>
</section>

<footer class="site-footer abs">COPYRIGHT © 2019 | INFO@KATZENHAIN-OBERLAU.CH</footer>

</body>
</html>
```